Flyer design for retail store owners

i would need to have a flyer design for my retail shop customers to show that I am a mailbox store that has all major shipping vendors to for their shipping needs. Ensuring that they can take advantage of opening a house account at the store and billed monthly, word document has all the details. Please use stock images for the notary public, passport photos, mailbox brass pictures of my actual mailboxes are listed in the pictures. I need to make it POP and WOW these retail store owners as I am using it to advertise the business

```html
<!DOCTYPE html>
<html lang="en">
<head>
<meta charset="utf-8">
<title>Swift Box &amp; Ship – Mailbox Rental Flyer</title>
<link rel="stylesheet" href="https://fonts.googleapis.com/css2?family=Montserrat:wght@400;500;600;700;800;900&display=swap">
<style>
  :root{
    --red:#e31b23;
    --black:#0d0d0d;
    --white:#ffffff;
    --ink:#1a1a1a;
    --stage:#2b2b2d;
    --brass-1:#d8b27a;
    --brass-2:#a97f44;
    --sky-1:#eef4fb;
    --sky-2:#a9c6e6;
    --sky-3:#6d93bf;
  }
  *{box-sizing:border-box;margin:0;padding:0}
  html,body{width:1200px;height:776px;overflow:hidden;background:var(--stage)}
  body{font-family:"Montserrat",Arial,sans-serif;color:var(--ink);position:relative}
  .page{position:absolute;top:28px;width:510px;height:720px;background:var(--white);overflow:hidden}
  .page--front{left:60px}
  .page--back{left:630px}

  /* ---------- front ---------- */
  .promo-band{position:absolute;top:22px;left:0;width:300px;height:96px;background:var(--red);color:var(--white);
    padding:14px 14px 0 18px;font-size:11px;font-weight:600;text-transform:uppercase;letter-spacing:.6px;line-height:1.3}
  .promo-band strong{font-weight:900}
  .mailbox-photo{position:absolute;top:12px;left:312px;width:182px;height:128px;
    background:linear-gradient(135deg,var(--brass-1),var(--brass-2) 60%,#7d5a2a)}
  .headline{position:absolute;top:128px;left:36px;font-weight:900;text-transform:uppercase;letter-spacing:-3px;line-height:.86}
  .headline__line{display:block;color:var(--black);font-size:82px}
  .headline__line--red{color:var(--red);font-size:71px;letter-spacing:-2.5px;margin-top:2px}
  .headline__sub{position:absolute;top:338px;left:40px;font-size:15.5px;font-weight:900;text-transform:uppercase;letter-spacing:.2px}

  .offer-pill{position:absolute;top:372px;left:150px;width:345px;height:138px;background:var(--red);border-radius:69px;
    padding:14px 0 0 64px;color:var(--white)}
  .offer-pill__title{font-size:17px;font-weight:900;text-transform:uppercase;margin-bottom:4px}
  .offer-pill__list{list-style:none;font-size:11.5px;font-weight:600;line-height:1.5}
  .offer-pill__list li{display:flex;align-items:center;gap:6px}
  .tick{flex:none;width:12px;height:12px}
  .price-badge{position:absolute;top:364px;left:34px;width:152px;height:152px;border-radius:50%;background:var(--black);
    color:var(--white);text-align:center;padding-top:22px}
  .price-badge__amount{font-size:56px;font-weight:900;letter-spacing:-2px;line-height:1}
  .price-badge__terms{font-size:13px;font-weight:600;text-transform:uppercase;line-height:1.15;margin-top:6px}

  .perks{position:absolute;top:520px;left:36px;width:450px;height:112px;display:flex;gap:14px;font-size:9px;line-height:1.3;font-weight:500}
  .perks__col{flex:1}
  .perks__col + .perks__col{border-left:2px solid #c9c9c9;padding-left:12px}
  .perks p{margin-bottom:2px}
  .perks .tick{width:9px;height:9px;display:inline-block;vertical-align:-1px;margin-right:3px}

  .footer-bar{position:absolute;left:0;bottom:0;width:100%;height:78px;background:var(--black)}
  .cta{position:absolute;background:var(--red);color:var(--white);font-weight:900;text-transform:uppercase;
    font-size:14px;line-height:1.15;padding:12px 14px;letter-spacing:.2px}
  .page--front .cta{left:44px;bottom:0;width:172px;height:86px}
  .contact{position:absolute;font-size:10px;font-weight:500;line-height:1.9;white-space:nowrap}
  .contact__row{display:flex;gap:10px}
  .contact span{display:inline-flex;align-items:center;gap:4px}
  .contact svg{width:10px;height:10px;flex:none}
  .page--front .contact{left:226px;bottom:20px;color:var(--white)}

  /* ---------- back ---------- */
  .top-band{position:absolute;top:0;left:0;width:100%;height:122px;background:var(--red);color:var(--white);
    display:flex;align-items:center;justify-content:center;text-align:center;font-size:17px;font-weight:800;
    text-transform:uppercase;line-height:1.15;letter-spacing:.6px;padding:0 40px}
  .cabinet-photo{position:absolute;top:140px;left:32px;width:148px;height:140px;
    background:linear-gradient(135deg,#e3c592,var(--brass-2))}
  .intro-copy{position:absolute;top:138px;left:196px;width:290px;font-size:10.4px;line-height:1.45;text-align:justify;font-weight:500}
  .brand-tag{position:absolute;top:300px;left:40px;width:104px;height:46px;background:var(--red);color:var(--white);
    font-size:11.5px;font-weight:800;text-transform:uppercase;letter-spacing:1px;text-align:center;line-height:1.3;padding-top:9px}
  .slogan-box{position:absolute;top:294px;left:150px;width:330px;height:58px;border:3px solid var(--black);
    display:flex;align-items:center;justify-content:center;text-align:center;font-size:14.5px;font-weight:900;text-transform:uppercase;line-height:1.1}
  .service-copy{position:absolute;top:372px;left:44px;width:424px;text-align:center;font-size:10.8px;line-height:1.45;font-weight:500}
  .service-copy strong{color:var(--red);font-weight:800;text-transform:uppercase}
  .sky-photo{position:absolute;left:0;top:462px;width:100%;height:258px;
    background:linear-gradient(180deg,var(--white) 0%,var(--sky-1) 20%,var(--sky-2) 65%,var(--sky-3) 100%)}
  .partner-strip{position:absolute;top:490px;left:90px;width:330px;height:36px;background:var(--white);border-radius:18px;
    box-shadow:0 1px 4px rgba(0,0,0,.2);display:flex;align-items:center;justify-content:space-around;padding:0 14px}
  .partner-badge{width:62px;height:20px;border-radius:3px}
  .page--back .cta{left:30px;bottom:0;width:172px;height:84px}
  .page--back .contact{left:212px;bottom:22px;color:var(--ink)}
</style>
</head>
<body>

<section class="page page--front">
  <div class="promo-band">We are offering all Maple Grove Plaza owners / employees an <strong>exclusive promo deal!</strong></div>
  <div class="mailbox-photo" role="img" aria-label="Brass mailbox doors with one door open"></div>

  <h1 class="headline">
    <span class="headline__line">Now</span>
    <span class="headline__line">Renting</span>
    <span class="headline__line headline__line--red">Mailboxes</span>
  </h1>
  <p class="headline__sub">On Maple Grove Plaza</p>

  <div class="offer-pill">
    <p class="offer-pill__title">You Get...</p>
    <ul class="offer-pill__list">
      <li><svg class="tick" viewBox="0 0 12 12"><circle cx="6" cy="6" r="6" fill="#fff"/><path d="M3.2 6.2l2 2 3.6-4" stroke="#e31b23" stroke-width="1.6" fill="none"/></svg>A Mailbox In The Shop</li>
      <li><svg class="tick" viewBox="0 0 12 12"><circle cx="6" cy="6" r="6" fill="#fff"/><path d="M3.2 6.2l2 2 3.6-4" stroke="#e31b23" stroke-width="1.6" fill="none"/></svg>A Book Of Stamps (20 Count)</li>
      <li><svg class="tick" viewBox="0 0 12 12"><circle cx="6" cy="6" r="6" fill="#fff"/><path d="M3.2 6.2l2 2 3.6-4" stroke="#e31b23" stroke-width="1.6" fill="none"/></svg>3 Notarizations By Appointment</li>
      <li><svg class="tick" viewBox="0 0 12 12"><circle cx="6" cy="6" r="6" fill="#fff"/><path d="M3.2 6.2l2 2 3.6-4" stroke="#e31b23" stroke-width="1.6" fill="none"/></svg>100 Copies Of Black And White</li>
      <li><svg class="tick" viewBox="0 0 12 12"><circle cx="6" cy="6" r="6" fill="#fff"/><path d="M3.2 6.2l2 2 3.6-4" stroke="#e31b23" stroke-width="1.6" fill="none"/></svg>100 Copies Of Color.</li>
    </ul>
  </div>
  <div class="price-badge">
    <div class="price-badge__amount">$12</div>
    <div class="price-badge__terms">A month for<br>6-12 months<br>leases!</div>
  </div>

  <div class="perks">
    <div class="perks__col">
      <p><svg class="tick" viewBox="0 0 12 12"><circle cx="6" cy="6" r="6" fill="#e31b23"/><path d="M3.2 6.2l2 2 3.6-4" stroke="#fff" stroke-width="1.6" fill="none"/></svg>As a retail owner, you know how important it is to keep your customers coming back - you will get <strong>20% discount for printing services.</strong></p>
      <p><svg class="tick" viewBox="0 0 12 12"><circle cx="6" cy="6" r="6" fill="#e31b23"/><path d="M3.2 6.2l2 2 3.6-4" stroke="#fff" stroke-width="1.6" fill="none"/></svg>We duplicate keys for $2/each, our regular price charge is $4/each. <strong>Save up to 50%!</strong></p>
      <p><svg class="tick" viewBox="0 0 12 12"><circle cx="6" cy="6" r="6" fill="#e31b23"/><path d="M3.2 6.2l2 2 3.6-4" stroke="#fff" stroke-width="1.6" fill="none"/></svg>Lamination is also discounted at 10% off.</p>
    </div>
    <div class="perks__col">
      <p><svg class="tick" viewBox="0 0 12 12"><circle cx="6" cy="6" r="6" fill="#e31b23"/><path d="M3.2 6.2l2 2 3.6-4" stroke="#fff" stroke-width="1.6" fill="none"/></svg><strong>10% off retail supplies</strong> ... must be minimum of 10$</p>
      <p><svg class="tick" viewBox="0 0 12 12"><circle cx="6" cy="6" r="6" fill="#e31b23"/><path d="M3.2 6.2l2 2 3.6-4" stroke="#fff" stroke-width="1.6" fill="none"/></svg>For house accounts - a 5% discount will be deducted monthly of billing change to invoicing PLUS we're giving another 5% of the discount if you upgrade and sign up for mailbox. Great right?</p>
    </div>
  </div>

  <div class="footer-bar"></div>
  <div class="cta">Take advantage of this limited time offer now!</div>
  <div class="contact">
    <div class="contact__row">
      <span><svg viewBox="0 0 10 10"><path d="M2 0.5l2 2-1 1.2c.6 1.3 1.5 2.2 2.8 2.8l1.2-1 2 2-1.3 1.8C4.5 9.2.8 5.5 .5 1.8z" fill="currentColor"/></svg>555-014-2290</span>
      <span><svg viewBox="0 0 10 10"><path d="M5 0a3.5 3.5 0 0 0-3.5 3.5C1.5 6 5 10 5 10s3.5-4 3.5-6.5A3.5 3.5 0 0 0 5 0zm0 5a1.4 1.4 0 1 1 0-2.8A1.4 1.4 0 0 1 5 5z" fill="currentColor"/></svg>48 Harbor Ave, Troy, NY 12180</span>
    </div>
    <div class="contact__row">
      <span><svg viewBox="0 0 10 10"><path d="M0 2h10v6H0z M0 2l5 3.5L10 2" stroke="currentColor" fill="none"/></svg>info@swiftbox.example</span>
      <span><svg viewBox="0 0 10 10"><circle cx="5" cy="5" r="4.4" stroke="currentColor" fill="none"/><path d="M.6 5h8.8M5 .6c-2.4 2.8-2.4 6 0 8.8M5 .6c2.4 2.8 2.4 6 0 8.8" stroke="currentColor" fill="none"/></svg>swiftbox.example</span>
    </div>
  </div>
</section>

<section class="page page--back">
  <h2 class="top-band">Renting a mail box is one of the most efficient and cost saving methods for receiving your mail and packages.</h2>
  <div class="cabinet-photo" role="img" aria-label="Brass cabinet of rental mailboxes"></div>
  <p class="intro-copy">Instead of having to worry about private security, weather conditions, sorting, and deliveries; all you have to do is pick-up your mail from our secured facility each day except Sundays. You will get a notification when mail arrives whether envelope or package, it will be scanned in daily which other mailbox stores do not offer! We offer onsite Notary Public with no appointments and onsite Passport Photos and can ship out same day.</p>

  <div class="brand-tag">Swift Box<br>&amp; Ship</div>
  <div class="slogan-box">We make your shipping<br>experience convenient</div>

  <p class="service-copy">At Swift Box &amp; Ship, whether you are shipping packages, documents, or packages, we are here to help. Whether you want to track your package or estimate the price of your package, it is easy for you. We are ready to handle all of your postal services! Get also the services you need; printing, copying, and stop in to purchase postage or shipping materials. <strong>Service point partners are;</strong></p>

  <div class="sky-photo" role="img" aria-label="Cargo airplane flying above the clouds"></div>
  <div class="partner-strip">
    <span class="partner-badge" style="background:#5a3b1e"></span>
    <span class="partner-badge" style="background:#4d2c8c"></span>
    <span class="partner-badge" style="background:#2a4d8f"></span>
    <span class="partner-badge" style="background:#f2c200"></span>
  </div>

  <div class="cta">Take advantage of this limited time offer now!</div>
  <div class="contact">
    <div class="contact__row">
      <span><svg viewBox="0 0 10 10"><path d="M2 0.5l2 2-1 1.2c.6 1.3 1.5 2.2 2.8 2.8l1.2-1 2 2-1.3 1.8C4.5 9.2.8 5.5 .5 1.8z" fill="currentColor"/></svg>555-014-2290</span>
      <span><svg viewBox="0 0 10 10"><path d="M5 0a3.5 3.5 0 0 0-3.5 3.5C1.5 6 5 10 5 10s3.5-4 3.5-6.5A3.5 3.5 0 0 0 5 0zm0 5a1.4 1.4 0 1 1 0-2.8A1.4 1.4 0 0 1 5 5z" fill="currentColor"/></svg>48 Harbor Ave, Troy, NY 12180</span>
    </div>
    <div class="contact__row">
      <span><svg viewBox="0 0 10 10"><path d="M0 2h10v6H0z M0 2l5 3.5L10 2" stroke="currentColor" fill="none"/></svg>info@swiftbox.example</span>
      <span><svg viewBox="0 0 10 10"><circle cx="5" cy="5" r="4.4" stroke="currentColor" fill="none"/><path d="M.6 5h8.8M5 .6c-2.4 2.8-2.4 6 0 8.8M5 .6c2.4 2.8 2.4 6 0 8.8" stroke="currentColor" fill="none"/></svg>swiftbox.example</span>
    </div>
  </div>
</section>

</body>
</html>
```